Zielgruppe
wir sind ein ambulanter Pflegedienst
Aufgabenstellung
Es soll ein Flyer entworfen werden.
Im Vordergrund steht die Behandlungspflege. Patienten sollen darauf aufmerksam gemacht werden, dass wir Insulininjektionen übernehmen und Kompressionsstrümpfe anziehen, wenn der Hausarzt dafür eine Verordnung ausstellt.
Im Vordergrund steht die Insulininjektion und das an und ausziehen der Kompressionsstrümpfe.
Falls die Patienten es nicht mehr alleine schaffen, springt der Pflegedienst ein.
Wichtig ist, dass das Pflegegeld nicht gekürzt wird, da dies eine Leistung der Krankenkasse ist.
Daten des Pflegedienstes:
Pflegehaus Lindental
Birkenweg 27
18057 Rostock
Tel 0800 4417236
www.Pflegehaus-Lindental.de
info@Pflegehaus-Lindental.de

```html
<!DOCTYPE html>
<html lang="de">
<head>
<meta charset="utf-8">
<title>Behandlungspflege – Pflegehaus Lindental</title>
<link href="https://fonts.googleapis.com/css2?family=Arimo:wght@400;700&display=swap" rel="stylesheet">
<style>
  :root {
    --green: #62ad32;
    --orange: #f08a24;
    --text: #555555;
    --white: #ffffff;
    --backdrop: #e9e9e9;
    --navy: #1f3f8f;
  }
  * { margin: 0; padding: 0; box-sizing: border-box; }
  html, body { width: 1200px; height: 675px; overflow: hidden; background: var(--backdrop); }
  body { font-family: "Arimo", Arial, sans-serif; }

  .flyer {
    position: absolute; left: 130px; top: 6px;
    width: 940px; height: 663px;
    background: var(--white); overflow: hidden;
  }
  .header-band {
    position: absolute; left: 221px; top: 0; width: 565px; height: 121px;
    background: var(--green);
  }
  .header-title {
    position: absolute; left: 330px; top: 50px; width: 490px; text-align: center;
    color: var(--white); font-size: 39px; font-weight: 700; letter-spacing: -0.3px;
  }
  .brand {
    position: absolute; left: 790px; top: 30px; width: 150px; text-align: center;
    color: var(--green); font-size: 14px; font-weight: 700; line-height: 1.2;
  }
  .brand-dot {
    display: block; width: 54px; height: 54px; margin: 0 auto 8px;
    border: 4px solid var(--navy); border-radius: 50%;
  }
  .artwork { position: absolute; left: 0; top: 0; }

  .content { position: absolute; left: 470px; top: 0; width: 440px; color: var(--text); font-weight: 700; font-size: 14px; line-height: 16px; }
  .content p { position: absolute; left: 0; width: 400px; }
  .section-title {
    position: absolute; left: 470px; top: 138px;
    color: var(--green); font-size: 33px; font-weight: 700;
    text-decoration: underline; text-decoration-thickness: 2px; text-underline-offset: 4px;
  }
  .services { position: absolute; left: 38px; top: 296px; list-style: none; color: var(--orange); font-size: 17.5px; line-height: 20px; }
  .services li { margin-bottom: 11px; white-space: nowrap; }
  .services li::before { content: "•"; margin-right: 3px; }

  .phone-band {
    position: absolute; left: 0; top: 613px; width: 940px; height: 50px;
    background: var(--orange);
  }
  .phone-line {
    position: absolute; left: 430px; top: 622px; display: flex; align-items: center; gap: 12px;
    color: var(--white); font-size: 27px; font-weight: 700; white-space: nowrap;
  }
</style>
</head>
<body>
<div class="flyer">
  <div class="header-band"></div>
  <h1 class="header-title">Behandlungspflege</h1>

  <div class="brand"><span class="brand-dot"></span>Pflegehaus Lindental</div>

  <div class="phone-band"></div>

  <svg class="artwork" width="940" height="663" viewBox="0 0 940 663">
    <defs>
      <linearGradient id="skin" x1="0" y1="0" x2="1" y2="1">
        <stop offset="0" stop-color="#f3ece6"/>
        <stop offset="0.35" stop-color="#e0ad8a"/>
        <stop offset="1" stop-color="#b87b58"/>
      </linearGradient>
      <linearGradient id="stocking" x1="0" y1="0" x2="1" y2="1">
        <stop offset="0" stop-color="#ffffff"/>
        <stop offset="1" stop-color="#f1ece7"/>
      </linearGradient>
    </defs>
    <circle cx="100" cy="331" r="352" fill="url(#skin)" stroke="var(--orange)" stroke-width="10"
            role="img" aria-label="Foto: Pflegekraft setzt eine Insulinspritze am Bauch"/>
    <circle cx="113" cy="564" r="116" fill="url(#stocking)" stroke="var(--orange)" stroke-width="6"
            role="img" aria-label="Foto: hautfarbener Kompressionsstrumpf"/>
    <ellipse cx="120" cy="575" rx="70" ry="48" fill="#dcae83" opacity="0.55" aria-hidden="true"/>
  </svg>

  <h2 class="section-title">Unsere Leistungen:</h2>

  <div class="content">
    <p style="top:186px">Mit unserem Fachpersonal sind wir vom ambulanten Pflegehaus Lindental Ihre Experten für ärztlich verordnete Behandlungen.</p>
    <p style="top:250px">Als auf Diabetes Patienten spezialisierter Pflegedienst übernehmen wir auch</p>
    <ul class="services">
      <li>Insulininjektionen und Blutzuckerkontrollen</li>
      <li>Kompressionsstrümpfe an- und ausziehen</li>
    </ul>
    <p style="top:361px">und weitere med. Behandlungspflegen nach neuesten, fachlichen Erkenntnissen.</p>
    <p style="top:408px">Das Pflegegeld wird nicht gekürzt, da dies eine Leistung der Krankenkasse ist.</p>
    <p style="top:456px">Informieren Sie sich unter:</p>
    <p style="top:487px">Pflegehaus Lindental<br>Birkenweg 27<br>18057 Rostock<br>Tel.:&nbsp; 0800 4417236 (kostenfrei)</p>
    <p style="top:566px">www.Pflegehaus-Lindental.de<br>info@Pflegehaus-Lindental.de</p>
  </div>

  <div class="phone-line">
    <svg width="32" height="32" viewBox="0 0 32 32" aria-hidden="true">
      <circle cx="16" cy="16" r="14.5" fill="none" stroke="#1a1a1a" stroke-width="2.5"/>
      <path d="M11 8.5c1-.6 2-.3 2.5.7l1.4 2.8c.4.8.1 1.6-.6 2.1l-1 .7c.8 2 2.4 3.6 4.4 4.6l.8-1c.5-.7 1.4-.9 2.1-.5l2.7 1.5c1 .5 1.2 1.6.6 2.5-1.1 1.7-3 2.4-5 1.6-4.4-1.8-7.6-5.2-9-9.6-.6-1.9.1-4 1.6-4.9z" fill="#1a1a1a"/>
    </svg>
    <span>0800 44172 36 (kostenfrei)</span>
  </div>
</div>
</body>
</html>
```